Agriculture Business Need a Responsive Web Design

We need a Responsive Web Design for a Agriculture Business
We deliver agriculture data insight for farmers, media, salespersons and other that have an interrest in Agriculture.
Our products is a Velmorix - a application that helps people with insight on farms, and what this farms have deliveried of products. Products like Milk, grains, eggs, slaughtering of livestock, chicken, sheep and other slaughter of animals. Data about size of farms. We deliver stats about these farms. Compeare farms.

Target Market(s)

Agriculture businesses

Industry/Entity Type

Agriculture

Number of Pages Required

1 page

Font styles to use
Sans Serif

Requirements
Must have
• Responsive design. I.e the design shall be used on smartphones to desktop browsers. I think 2 columns on big screens that will collapse to 1 one small screens.

```html
<!DOCTYPE html>
<html lang="en">
<head>
<meta charset="utf-8">
<title>Velmorix Enterprise</title>
<link rel="stylesheet" href="https://fonts.googleapis.com/css2?family=Raleway:wght@400;500;600;700&display=swap">
<style>
:root{
  --blue:#159ee0;
  --blue-dark:#0c86c4;
  --green:#5aae3a;
  --ink:#2b2b2b;
  --text:#555;
  --muted:#777;
  --line:#e3e3e3;
  --white:#fff;
  --footer:#333;
}
*{box-sizing:border-box;margin:0;padding:0}
html,body{width:1200px;height:2821px;overflow:hidden}
body{position:relative;font-family:"Raleway",Arial,sans-serif;color:var(--text);background:var(--white)}
.abs{position:absolute}

/* header */
.site-header{left:0;top:0;width:1200px;height:94px;background:var(--white)}
.brand{left:100px;top:22px;display:flex;align-items:center;gap:12px}
.brand-dot{width:36px;height:36px;border-radius:50%;background:var(--green)}
.brand-name{font-size:27px;font-weight:600;line-height:1.05;color:var(--blue);width:230px}
.call{right:100px;top:16px;font-size:12px;color:var(--muted);display:flex;align-items:center;gap:8px}
.call strong{font-size:17px;color:var(--ink);font-weight:700}
.call svg{width:20px;height:20px}
.main-nav{right:100px;top:54px;display:flex;gap:34px;font-size:14.5px;font-weight:500;color:#444;text-transform:uppercase;letter-spacing:.3px}
.main-nav .active{color:var(--blue);border-bottom:2px solid var(--blue);padding-bottom:5px}

/* hero */
.hero{left:0;top:94px;width:1200px;height:470px;background:linear-gradient(180deg,#e7b66a 0%,#c78b3e 35%,#8a8c3c 62%,#6f9a2c 80%,#557e1f 100%)}
.hero-title{left:476px;top:210px;font-size:33px;font-weight:700;color:var(--white);line-height:1.25;text-transform:uppercase;text-shadow:0 2px 4px rgba(0,0,0,.35)}
.slide-arrow{top:309px;width:40px;height:40px;border-radius:50%;background:rgba(30,30,30,.85)}
.slide-arrow svg{width:40px;height:40px}

/* shared headings */
.section-title{left:0;width:1200px;text-align:center;font-size:38px;font-weight:400;color:var(--ink);text-transform:uppercase;letter-spacing:.5px}
.section-title b{font-weight:700}
.lead{left:0;width:1200px;text-align:center;font-size:14px;line-height:24px;color:var(--text)}
.btn{background:var(--blue);color:var(--white);font-weight:700;text-transform:uppercase;text-align:center;border-bottom:3px solid var(--blue-dark);letter-spacing:.4px}

/* about */
.about-title{top:610px}
.about-title .accent{color:var(--blue);font-weight:700}
.about-title .brand-accent{color:var(--blue);font-weight:700}
.about-text{top:680px;left:190px;width:820px}
.read-more{left:536px;top:794px;width:128px;height:41px;line-height:39px;font-size:14px}

/* features */
.features{left:0;top:888px;width:1200px;height:641px;background:radial-gradient(ellipse at 30% 30%,#8fbf55 0%,#3f8a3d 40%,#1f5f4a 75%,#2a4f4a 100%)}
.features-title{top:940px;color:var(--white)}
.feature-device{left:502px;top:1025px;width:205px;height:438px;border-radius:30px;background:linear-gradient(180deg,#2d2d2d,#111)}
.feature-icon{width:72px;height:72px;border-radius:50%;background:var(--white)}
.feature-icon svg{width:72px;height:72px}
.feature-link{height:0;border-top:2px dashed rgba(255,255,255,.85)}
.feature-dot{width:12px;height:12px;border-radius:50%;background:var(--white)}
.feature-text{width:240px;color:var(--white)}
.feature-text h3{font-size:22px;font-weight:400;text-transform:uppercase;margin-bottom:6px}
.feature-text p{font-size:13px;line-height:20px}
.feature-text.left{text-align:right}

/* what we do */
.do-title{top:1575px}
.do-text{top:1643px}
.tablet{left:107px;top:1725px;width:421px;height:321px;border-radius:18px;background:#f6f6f6;border:2px solid #ddd}
.tablet-screen{left:40px;top:22px;width:340px;height:275px;background:linear-gradient(90deg,#3a3a3a 0 27%,#f4f8fa 27% 100%)}
.tablet-screen::after{content:"";position:absolute;left:27%;top:0;width:73%;height:40px;background:#1fb7c6}
.pager{top:2064px;width:14px;height:14px;border-radius:50%;background:#cfcfcf}
.pager.on{background:var(--blue)}
.do-list{left:551px;top:1740px;width:549px;list-style:none}
.do-list li{position:relative;height:78px;padding-left:33px;border-bottom:1px solid var(--line);padding-top:4px}
.do-list svg{position:absolute;left:0;top:6px;width:20px;height:20px}
.do-list h4{font-size:18px;font-weight:700;color:var(--blue);margin-bottom:9px}
.do-list p{font-size:13px;color:var(--text)}

/* call to action */
.cta{left:0;top:2139px;width:1200px;height:325px;background:linear-gradient(180deg,#22446e 0%,#4f7fb3 35%,#9dbbd5 55%,#7c9a4a 72%,#4f6e25 100%)}
.cta-title{right:136px;top:2200px;font-size:40px;color:var(--white);text-align:right;font-weight:400}
.cta-title b{font-weight:700}
.cta-sub{right:136px;top:2268px;font-size:29px;line-height:40px;color:var(--white);text-align:right}
.cta-btn{left:807px;top:2370px;width:255px;height:47px;line-height:44px;font-size:16px}

/* newsletter */
.news-title{top:2517px}
.news-text{top:2580px;left:280px;width:640px}
.plane{left:205px;top:2670px;width:160px;height:110px;background:radial-gradient(ellipse at 30% 30%,rgba(90,174,58,.35),rgba(90,174,58,0) 70%)}
.signup{left:382px;top:2667px;display:flex}
.signup-input{width:410px;height:43px;border:1px solid #ddd;border-right:0;font-size:14px;color:#444;padding:0 13px;line-height:41px}
.signup-btn{width:169px;height:43px;line-height:41px;font-size:16px;display:flex;justify-content:center;align-items:center;gap:18px;border-bottom:0}
.signup-btn svg{width:18px;height:14px}

/* footer */
.site-footer{left:0;top:2765px;width:1200px;height:56px;background:var(--footer)}
.copyright{left:100px;top:20px;font-size:13px;color:#ddd}
.copyright b{color:var(--white)}
.social{top:15px;width:26px;height:26px;border-radius:50%;background:var(--white)}
</style>
</head>
<body>

<header class="site-header abs">
  <div class="brand abs">
    <span class="brand-dot"></span>
    <span class="brand-name">VELMORIX ENTERPRISE</span>
  </div>
  <div class="call abs">Call Us
    <svg viewBox="0 0 20 20"><circle cx="10" cy="10" r="9" fill="none" stroke="#5aae3a" stroke-width="1.5"/><path d="M7 5.5l2 2-1 1.2c.6 1.3 1.6 2.3 2.9 2.9l1.2-1 2 2-1.3 1.4c-3.3-.4-6.6-3.7-7-7z" fill="#5aae3a"/></svg>
    <strong>555-014-2290</strong>
  </div>
  <nav class="main-nav abs">
    <span class="active">Home</span><span>Who We Are</span><span>How It Works</span><span>What We Do</span><span>Pricing</span><span>Contact Us</span>
  </nav>
</header>

<section class="hero abs" role="img" aria-label="Photo of a hand holding a smartphone showing the app, in front of a tractor in a sunlit field"></section>
<h1 class="hero-title abs">An Application That Delivers<br>Agriculture Data Insight</h1>
<span class="slide-arrow abs" style="left:38px"><svg viewBox="0 0 40 40"><path d="M23 13l-7 7 7 7" fill="none" stroke="#fff" stroke-width="2.5"/></svg></span>
<span class="slide-arrow abs" style="left:1122px"><svg viewBox="0 0 40 40"><path d="M17 13l7 7-7 7" fill="none" stroke="#fff" stroke-width="2.5"/></svg></span>

<h2 class="section-title about-title abs">About <span class="brand-accent">Velmorix</span> Enterprise</h2>
<p class="lead about-text abs">Lorem ipsum dolor sit amet, consectetuer adipiscing elit, sed diam nonummy nibh euismod tincidunt ut laoreet dolore magna aliquam erat volutpat. Ut wisi enim ad minim veniam, quis nostrud exerci tation ullamcorper suscipit lobortis nisl ut aliquip ex ea commodo consequat. Lorem ipsum dolor sit amet, consectetuer adipiscing elit, sed diam nonummy nibh euismod tincidunt ut laoreet dolore magna aliquam erat volutpat. Ut wisi enim ad minim veniam, quis nostrud exerci tation ullamcorper</p>
<div class="btn read-more abs">Read More</div>

<section class="features abs" role="img" aria-label="Blurred photo of green foliage behind the feature list"></section>
<h2 class="section-title features-title abs">Our <b>Features</b></h2>
<div class="feature-device abs" role="img" aria-label="Smartphone showing the app start screen"></div>

<!-- connectors -->
<div class="feature-link abs" style="left:454px;top:1115px;width:48px"></div>
<div class="feature-link abs" style="left:454px;top:1256px;width:48px"></div>
<div class="feature-link abs" style="left:454px;top:1392px;width:48px"></div>
<div class="feature-link abs" style="left:707px;top:1115px;width:45px"></div>
<div class="feature-link abs" style="left:707px;top:1256px;width:45px"></div>
<div class="feature-link abs" style="left:707px;top:1392px;width:45px"></div>
<span class="feature-dot abs" style="left:496px;top:1110px"></span>
<span class="feature-dot abs" style="left:496px;top:1251px"></span>
<span class="feature-dot abs" style="left:496px;top:1387px"></span>
<span class="feature-dot abs" style="left:701px;top:1110px"></span>
<span class="feature-dot abs" style="left:701px;top:1251px"></span>
<span class="feature-dot abs" style="left:701px;top:1387px"></span>

<span class="feature-icon abs" style="left:382px;top:1079px"><svg viewBox="0 0 72 72"><circle cx="36" cy="36" r="30" fill="var(--blue)"/><path d="M33 48V30a3 3 0 016 0v9l7 2v8" fill="none" stroke="#fff" stroke-width="2.5" stroke-linejoin="round"/><circle cx="36" cy="28" r="8" fill="none" stroke="#fff" stroke-width="1.5"/></svg></span>
<span class="feature-icon abs" style="left:382px;top:1220px"><svg viewBox="0 0 72 72"><circle cx="36" cy="36" r="30" fill="var(--blue)"/><circle cx="31" cy="39" r="7" fill="none" stroke="#fff" stroke-width="3" stroke-dasharray="3 2"/><circle cx="31" cy="39" r="3" fill="#fff"/><circle cx="44" cy="28" r="5" fill="none" stroke="#fff" stroke-width="2.5" stroke-dasharray="2.5 1.5"/></svg></span>
<span class="feature-icon abs" style="left:382px;top:1356px"><svg viewBox="0 0 72 72"><circle cx="36" cy="36" r="30" fill="var(--blue)"/><rect x="26" y="22" width="20" height="28" rx="2" fill="none" stroke="#fff" stroke-width="2.5"/><path d="M30 30h12M30 36h12M30 42h8" stroke="#fff" stroke-width="2"/></svg></span>
<span class="feature-icon abs" style="left:752px;top:1079px"><svg viewBox="0 0 72 72"><circle cx="36" cy="36" r="30" fill="var(--blue)"/><path d="M25 48V40M31 48V36M37 48V32M43 48V27M49 48V23" stroke="#fff" stroke-width="4"/><path d="M24 34l12-8 6 3 9-7" fill="none" stroke="#fff" stroke-width="2"/></svg></span>
<span class="feature-icon abs" style="left:752px;top:1220px"><svg viewBox="0 0 72 72"><circle cx="36" cy="36" r="30" fill="var(--blue)"/><circle cx="36" cy="36" r="13" fill="none" stroke="#fff" stroke-width="2.5"/><path d="M23 36h26M36 23c-6 7-6 19 0 26M36 23c6 7 6 19 0 26" fill="none" stroke="#fff" stroke-width="2"/></svg></span>
<span class="feature-icon abs" style="left:752px;top:1356px"><svg viewBox="0 0 72 72"><circle cx="36" cy="36" r="30" fill="var(--blue)"/><rect x="26" y="33" width="20" height="16" rx="2" fill="#fff"/><path d="M30 33v-5a6 6 0 0112 0v5" fill="none" stroke="#fff" stroke-width="3"/><rect x="35" y="38" width="2" height="6" fill="var(--blue)"/></svg></span>

<div class="feature-text left abs" style="left:127px;top:1080px"><h3>Easy To Use</h3><p>Mattis porttitor nulla, eget gravida id . Nune sollicit udin</p></div>
<div class="feature-text left abs" style="left:127px;top:1218px"><h3>Functionality</h3><p>Mattis porttitor nulla, eget gravida id . Nune sollicit udin</p></div>
<div class="feature-text left abs" style="left:127px;top:1358px"><h3>Compatibility</h3><p>Mattis porttitor nulla, eget gravida id . Nune sollicit udin</p></div>
<div class="feature-text abs" style="left:842px;top:1080px"><h3>Performance</h3><p>Mattis porttitor nulla, eget gravida id . Nune sollicit udin</p></div>
<div class="feature-text abs" style="left:842px;top:1218px"><h3>Localization</h3><p>Mattis porttitor nulla, eget gravida id . Nune sollicit udin</p></div>
<div class="feature-text abs" style="left:842px;top:1358px"><h3>Security</h3><p>Mattis porttitor nulla, eget gravida id . Nune sollicit udin</p></div>

<h2 class="section-title do-title abs">What <b>We Do</b></h2>
<p class="lead do-text abs">Lorem ipsum dolor sit amet, consectetuer adipiscing elit, sed diam nonummy nibh euismod tincidunt ut laoreet dolore magna aliquam erat volutpat.<br>Ut wisi enim ad minim veniam, quis nostrud exerci tation ullamcorper suscipit lobortis nisl ut aliquip ex ea commodo consequat.</p>
<div class="tablet abs">
  <div class="tablet-screen abs" role="img" aria-label="Dashboard screen of the app with menu, line chart and figures"></div>
</div>
<span class="pager on abs" style="left:272px"></span>
<span class="pager abs" style="left:303px"></span>
<span class="pager abs" style="left:333px"></span>
<ul class="do-list abs">
  <li><svg viewBox="0 0 20 20"><circle cx="10" cy="10" r="10" fill="var(--green)"/><path d="M5.5 10l3 3 6-6" fill="none" stroke="#fff" stroke-width="2"/></svg><h4>Compare Farms</h4><p>Lorem ipsum dolor sit amet, consectetuer adipiscing elit, sed diam nonummy</p></li>
  <li><svg viewBox="0 0 20 20"><circle cx="10" cy="10" r="10" fill="var(--green)"/><path d="M5.5 10l3 3 6-6" fill="none" stroke="#fff" stroke-width="2"/></svg><h4>Get Real Insight on Agriculture</h4><p>Lorem ipsum dolor sit amet, consectetuer adipiscing elit, sed diam nonummy</p></li>
  <li><svg viewBox="0 0 20 20"><circle cx="10" cy="10" r="10" fill="var(--green)"/><path d="M5.5 10l3 3 6-6" fill="none" stroke="#fff" stroke-width="2"/></svg><h4>Delivery Estate</h4><p>Lorem ipsum dolor sit amet, consectetuer adipiscing elit, sed diam nonummy</p></li>
  <li><svg viewBox="0 0 20 20"><circle cx="10" cy="10" r="10" fill="var(--green)"/><path d="M5.5 10l3 3 6-6" fill="none" stroke="#fff" stroke-width="2"/></svg><h4>Farm Size Data</h4><p>Lorem ipsum dolor sit amet, consectetuer adipiscing elit, sed diam nonummy</p></li>
</ul>

<section class="cta abs" role="img" aria-label="Photo of hens by a wooden fence on open farmland under a blue sky"></section>
<h2 class="cta-title abs"><b>VELMORIX</b> ENTERPRISE</h2>
<p class="cta-sub abs">An Application That Helps People<br>With Insight On Agriculture</p>
<div class="btn cta-btn abs">Get Started With Us</div>

<h2 class="section-title news-title abs">Newsletter <b>Sign Up</b></h2>
<p class="lead news-text abs">Lorem ipsum dolor sit amet, consectetuer adipiscing elit, sed diam nonummy nibh euismod tincidunt ut laoreet dolore magna aliquam erat volutpat. Ut wisi enim ad minim veniam.</p>
<div class="plane abs" role="img" aria-label="Illustration of a green paper plane with a dotted flight path"></div>
<form class="signup abs">
  <div class="signup-input">Enter your email address</div>
  <div class="btn signup-btn">Subscribe <svg viewBox="0 0 18 14"><path d="M2 2l5 5-5 5M10 2l5 5-5 5" fill="none" stroke="#fff" stroke-width="2"/></svg></div>
</form>

<footer class="site-footer abs">
  <p class="copyright abs">Copyright © 2016 <b>VELMORIX ENTERPRISE</b> &nbsp;|&nbsp; All Rights Reserved.</p>
  <span class="social abs" style="left:978px"></span>
  <span class="social abs" style="left:1010px"></span>
  <span class="social abs" style="left:1042px"></span>
  <span class="social abs" style="left:1074px"></span>
</footer>

</body>
</html>
```